Saltmarsh Motocross Club. Sports club.

We are a family orientated Motocross Club in Abu Dhabi. We have 3 motocross tracks, Intermediate Track, Junior rack and E-track. We also have a School(Academy) and maintenance facility that caters for all motorbike services. We have a BBQ area with a 20x70 meter pool after a hot day of riding. We are busy adding a restaurant and bar in the next few weeks. We host 6 Club races in the season as well as the Crescent Ridge Championship. Therefore we will need a race calendar as well as race results page. The school have a dedicated school facility with bike rental, bike show room, gear rental and small shop. We have instructors that instruct kids from 4 years old to professional riders.

Target Market(s)

Motocross riders, kids from 4 years

Industry/Entity Type

extreme sports, motorsports motocross

Coding

Coded - Design and coding required

Number of Pages Required

5+ page

Font styles to use
Sans Serif

Colors

Designer to choose colors to be used in the design.

Requirements
Must have
• User Friendly, Easy to update, Calendar , online payment, race results, academy, facilities,
Nice to have
• Just an update it has to have a calendar with sides that shows whats happening on the day. We also need at the top of page the "open hours", " a next event" button, our partners button at the bottom of page a "News Page" "testimonials" with all the necessary links, social medial, address, contact details, etc.
Should not have
• no cartoons or any clipart please just photos

```html
<!DOCTYPE html>
<html lang="en">
<head>
<meta charset="utf-8">
<title>Saltmarsh Motocross Club</title>
<link href="https://fonts.googleapis.com/css2?family=Barlow+Condensed:ital,wght@0,700;0,800;1,800;1,900&family=Open+Sans:wght@400;600;700&display=swap" rel="stylesheet">
<style>
:root{
  --red:#e31b23;
  --red-dark:#b8121a;
  --ink:#151515;
  --dark:#0e0e0e;
  --grey:#f3f3f3;
  --mid:#6d6d6d;
  --line:#dcdcdc;
  --white:#ffffff;
  --head:"Barlow Condensed", "Arial Narrow", sans-serif;
  --body:"Open Sans", Arial, sans-serif;
}
*{box-sizing:border-box;margin:0;padding:0}
html,body{width:1200px;height:3320px;overflow:hidden}
body{font-family:var(--body);color:var(--ink);background:var(--white);position:relative}
a{color:inherit;text-decoration:none}
.btn{display:inline-block;background:var(--red);color:var(--white);font-family:var(--body);font-weight:700;font-size:13px;letter-spacing:.5px;padding:13px 26px;text-transform:uppercase;white-space:nowrap}
.btn-outline{background:var(--white);color:var(--red)}
.section-title{font-family:var(--head);font-style:italic;font-weight:900;text-transform:uppercase;font-size:42px;line-height:1;color:var(--ink)}
.wordmark{display:flex;align-items:center;gap:10px;font-family:var(--head);font-weight:800;font-size:26px;color:var(--white);text-transform:uppercase;white-space:nowrap}
.wordmark .dot{width:30px;height:30px;border-radius:50%;background:var(--red)}

/* hero */
.hero{position:relative;height:660px;overflow:hidden}
.hero-photo{position:absolute;inset:0;background:
  radial-gradient(ellipse 45% 55% at 68% 40%,rgba(210,150,90,.95) 0%,rgba(170,105,60,.7) 40%,rgba(0,0,0,0) 75%),
  radial-gradient(ellipse 60% 40% at 60% 95%,rgba(190,130,80,.8) 0%,rgba(0,0,0,0) 70%),
  linear-gradient(180deg,#2a1a10 0%,#5b3620 50%,#2b1a0f 100%)}
.hero-photo::after{content:"";position:absolute;inset:0;background:linear-gradient(90deg,rgba(0,0,0,.45) 0%,rgba(0,0,0,.1) 55%,rgba(0,0,0,0) 100%)}
.topbar{position:absolute;top:0;left:0;right:0;height:36px;background:rgba(0,0,0,.55);display:flex;align-items:center;justify-content:space-between;padding:0 80px;color:var(--white);font-size:12px;z-index:2}
.topbar .phone{display:flex;align-items:center;gap:8px;font-weight:600}
.topbar .socials{display:flex;gap:8px}
.topbar .socials span{width:18px;height:18px;border-radius:50%;background:rgba(255,255,255,.85)}
.navbar{position:absolute;top:36px;left:0;right:0;height:64px;display:flex;align-items:center;justify-content:space-between;padding:0 80px;z-index:2}
.navbar ul{list-style:none;display:flex;align-items:center;gap:22px;color:var(--white);font-size:12px;font-weight:600;text-transform:uppercase;white-space:nowrap}
.navbar .btn{padding:10px 18px;font-size:12px}
.hero-copy{position:absolute;left:160px;top:300px;width:460px;color:var(--white);z-index:2}
.hero-copy h1{font-family:var(--head);font-style:italic;font-weight:900;font-size:64px;line-height:.95;text-transform:uppercase}
.hero-copy p{font-size:13px;line-height:1.6;margin:16px 0 24px}

/* partners */
.partners{height:140px;display:flex;align-items:center;padding:0 160px;gap:36px}
.partners h3{font-family:var(--head);font-style:italic;font-weight:900;font-size:30px;text-transform:uppercase;white-space:nowrap;flex:none}
.partner-badges{display:flex;gap:30px;align-items:center;flex:1;justify-content:space-between}
.partner-badges span{width:66px;height:28px;background:#cfcfcf;border-radius:3px}

/* about */
.about{display:flex;gap:40px;padding:20px 120px 0 100px;height:320px}
.about-collage{position:relative;width:360px;height:280px;flex:none}
.about-collage .ph{position:absolute}
.about-copy{flex:1;padding-top:20px}
.about-copy .section-title{font-size:40px}
.about-copy p{font-size:12px;line-height:1.65;color:var(--mid);margin:14px 0}

/* results */
.results{padding:40px 140px 0;height:280px}
.result-cards{display:flex;gap:26px;margin-top:30px}
.result-card{flex:1;background:var(--white);box-shadow:0 4px 18px rgba(0,0,0,.12);padding:22px;display:flex;gap:16px;align-items:center}
.avatar{width:58px;height:58px;border-radius:50%;background:linear-gradient(135deg,#c9b8a6,#6d5a4a);flex:none}
.result-card h4{font-size:14px;font-weight:700}
.result-card small{display:block;font-size:11px;color:var(--mid);margin:3px 0}
.result-card .pts{font-size:11px;font-weight:700;color:var(--red)}

/* mission */
.mission{height:340px;text-align:center;padding:30px 120px 0}
.mission .section-title{font-size:40px;width:760px;margin:0 auto}
.mission p{font-size:12px;line-height:1.7;color:var(--mid);margin:22px 0 26px;text-align:left}

/* partner band */
.partner-band{position:relative;height:440px;overflow:hidden}
.partner-band .band-photo{position:absolute;inset:0;background:
  radial-gradient(ellipse 18% 45% at 12% 60%,rgba(200,210,60,.55) 0%,rgba(0,0,0,0) 70%),
  radial-gradient(ellipse 22% 50% at 88% 55%,rgba(230,120,170,.45) 0%,rgba(0,0,0,0) 70%),
  linear-gradient(180deg,#3a86c2 0%,#8cc0e0 45%,#d7e6ea 62%,#7d9a4e 80%,#5d7a36 100%)}
.partner-band .cut-top{position:absolute;top:0;left:0;right:0;height:90px;background:var(--white);clip-path:polygon(0 0,100% 0,100% 20%,0 100%)}
.partner-band .cut-bottom{position:absolute;bottom:0;left:0;right:0;height:90px;background:var(--white);clip-path:polygon(0 80%,100% 0,100% 100%,0 100%)}
.partner-copy{position:absolute;left:0;right:0;top:150px;text-align:center}
.partner-copy .section-title{font-size:44px}
.partner-copy p{font-size:12px;margin:8px 0 18px;color:var(--ink)}

/* news */
.news{height:460px;padding:30px 160px 0;text-align:center}
.news-grid{display:flex;gap:20px;margin-top:30px;text-align:center}
.news-card{width:205px}
.news-card .ph{height:180px}
.news-card h5{font-size:11px;font-weight:700;text-transform:uppercase;line-height:1.45;margin:12px 4px 6px}
.news-card time{font-size:10px;color:var(--red);font-weight:600}

/* split */
.split{display:flex;height:260px}
.split-half{flex:1;position:relative;overflow:hidden;color:var(--white);padding:56px 70px}
.split-half .ph{position:absolute;inset:0}
.split-half>*:not(.ph){position:relative}
.split-half h3{font-family:var(--head);font-style:italic;font-weight:900;font-size:40px;text-transform:uppercase}
.split-half p{font-size:12px;line-height:1.6;margin:8px 0 18px;width:300px}
.subscribe{display:flex;margin-top:22px}
.subscribe span{width:250px;height:42px;background:var(--white);color:#999;font-size:12px;display:flex;align-items:center;padding:0 14px}
.subscribe .btn{padding:13px 22px}

/* footer */
.footer{background:var(--dark);color:#cfcfcf;height:420px;position:relative;padding:60px 100px 0}
.footer-cols{display:flex;gap:60px}
.footer-brand{width:300px}
.footer-brand p{font-size:12px;line-height:1.7;margin:18px 0}
.footer-brand .socials{display:flex;gap:10px}
.footer-brand .socials span{width:26px;height:26px;border-radius:50%;background:#3a3a3a}
.footer-col h4{font-family:var(--head);font-style:italic;font-weight:900;font-size:26px;color:var(--white);text-transform:uppercase;margin-bottom:14px}
.footer-col ul{list-style:none;font-size:11px;line-height:2.1;text-transform:uppercase}
.footer-col{width:160px}
.copyright{position:absolute;left:0;right:0;bottom:0;height:56px;border-top:1px solid #2a2a2a;display:flex;align-items:center;justify-content:center;font-size:11px;color:#8a8a8a}
.to-top{position:absolute;right:50px;bottom:10px;width:36px;height:36px;border-radius:50%;background:var(--red);display:flex;align-items:center;justify-content:center}
</style>
</head>
<body>

<header class="hero">
  <div class="hero-photo" role="img" aria-label="Motocross rider jumping over a dusty desert track"></div>
  <div class="topbar">
    <div class="phone">
      <svg width="12" height="12" viewBox="0 0 24 24"><path fill="#fff" d="M6.6 10.8a15.2 15.2 0 006.6 6.6l2.2-2.2a1 1 0 011-.25 11.4 11.4 0 003.6.6 1 1 0 011 1V20a1 1 0 01-1 1A17 17 0 013 4a1 1 0 011-1h3.5a1 1 0 011 1c0 1.25.2 2.45.6 3.6a1 1 0 01-.25 1z"/></svg>
      (02) 555 0147
    </div>
    <div class="socials"><span></span><span></span><span></span><span></span></div>
  </div>
  <nav class="navbar">
    <a class="wordmark" href="#"><span class="dot"></span>Saltmarsh</a>
    <ul>
      <li>Home</li><li>School</li><li>Motocross Club</li><li>Safety Course</li><li>Motocross Dubai</li><li>Contact</li>
      <li><a class="btn" href="#">Login/Register</a></li>
    </ul>
  </nav>
  <div class="hero-copy">
    <h1>Off-Road<br>Training School</h1>
    <p>Our trails are all wild and shaped by the forces of nature, with a fine balancing blend from our instructors. We know and believe that the outback trail is a far better teacher than any artificially created obstacle course.</p>
    <a class="btn btn-outline" href="#">Motocross Club</a>
  </div>
</header>

<section class="partners">
  <h3>Partners :</h3>
  <div class="partner-badges"><span></span><span></span><span></span><span></span><span></span><span></span><span></span><span></span></div>
</section>

<section class="about">
  <div class="about-collage">
    <div class="ph" style="left:0;top:0;width:130px;height:160px;background:linear-gradient(160deg,#d9dde2 0%,#8f9aa6 55%,#4c4032 100%)" role="img" aria-label="Young rider on a motocross bike"></div>
    <div class="ph" style="left:140px;top:0;width:220px;height:130px;background:linear-gradient(160deg,#e8e4dc 0%,#b5ab9c 50%,#5a5048 100%)" role="img" aria-label="Club members at the trophy ceremony"></div>
    <div class="ph" style="left:0;top:170px;width:130px;height:110px;background:linear-gradient(160deg,#f0efeb 0%,#bdb6aa 55%,#6a5f52 100%)" role="img" aria-label="Instructors at the club house"></div>
    <div class="ph" style="left:140px;top:140px;width:220px;height:140px;background:linear-gradient(160deg,#c7ccd2 0%,#7d8792 50%,#2f3338 100%)" role="img" aria-label="Bike showroom at the academy"></div>
  </div>
  <div class="about-copy">
    <h2 class="section-title">Read About Saltmarsh Motocross Club</h2>
    <p>Welcome! Our racing academy teaches safe motocross riding skills to beginner and advanced riders of all ages. We believe that the more knowledge you have, the better decisions you'll make and the safer you'll be. Our goal is to help you make quality decisions in all your riding endeavours, regardless of whether you've never ridden before or you're an experienced rider.</p>
    <p>Our racing academy is led by instructors with years of track experience and riders from the Crescent Ridge Championship, most recently in the 70+ class.</p>
    <a class="btn" href="#">Read More</a>
  </div>
</section>

<section class="results">
  <h2 class="section-title">Race Results</h2>
  <div class="result-cards">
    <div class="result-card"><div class="avatar" role="img" aria-label="Rider portrait"></div><div><h4>Liam Carver</h4><small>Abu Dhabi, United Arab Emirates</small><span class="pts">250 pts</span></div></div>
    <div class="result-card"><div class="avatar" role="img" aria-label="Rider portrait"></div><div><h4>R.J. Hollis</h4><small>Abu Dhabi, United Arab Emirates</small><span class="pts">236 pts</span></div></div>
    <div class="result-card"><div class="avatar" role="img" aria-label="Rider portrait"></div><div><h4>Omar Faris</h4><small>Abu Dhabi, United Arab Emirates</small><span class="pts">221 pts</span></div></div>
  </div>
</section>

<section class="mission">
  <h2 class="section-title">SMX — We Live Motocross, Enduro and Off-Road Motorcycling</h2>
  <p>Approximately 70% of our current participants start from zero, not knowing how to ride a motorcycle. But after just one day they normally understand the basics of motocross riding and can take on a track at our motocross courses. We categorise the participants in different off-road experience groups to make each session interesting, challenging and a rewarding experience. Whether you want to learn the right technique, build confidence for your first race or simply enjoy a weekend of riding, our instructors will put together the optimal drill plan and motocross training for you.</p>
  <a class="btn" href="#">Learn More</a>
</section>

<section class="partner-band">
  <div class="band-photo" role="img" aria-label="Motocross riders racing side by side under a blue sky"></div>
  <div class="cut-top"></div>
  <div class="cut-bottom"></div>
  <div class="partner-copy">
    <h2 class="section-title">Become Our Partner</h2>
    <p>Fill out the form below and we'll get in touch with you shortly.</p>
    <a class="btn" href="#">Get Started</a>
  </div>
</section>

<section class="news">
  <h2 class="section-title">Latest News Articles</h2>
  <div class="news-grid">
    <article class="news-card"><div class="ph" role="img" aria-label="Rider cornering on a dirt track" style="background:linear-gradient(170deg,#e6d9c4 0%,#b59a6e 50%,#6b5232 100%)"></div><h5>Motocross requirements and riding techniques in detail, things most riders never learn</h5><time>July 2019</time></article>
    <article class="news-card"><div class="ph" role="img" aria-label="Young riders lined up at the start gate" style="background:linear-gradient(170deg,#f2eee6 0%,#c4b59c 45%,#7a6a52 100%)"></div><h5>Women are also riding motocross at home, with our personal MX coach you learn how</h5><time>July 2019</time></article>
    <article class="news-card"><div class="ph" role="img" aria-label="Kids training on small motocross bikes" style="background:linear-gradient(170deg,#d7c8b0 0%,#a2563a 50%,#3d3a52 100%)"></div><h5>Extensive individual motocross instruction for children from five years of age</h5><time>June 2019</time></article>
    <article class="news-card"><div class="ph" role="img" aria-label="Instructor coaching a rider at the track" style="background:linear-gradient(170deg,#cfd6da 0%,#7c8a96 45%,#2f3a44 100%)"></div><h5>Riding course in the desert and coaching training in different groups for beginners</h5><time>March 2019</time></article>
  </div>
</section>

<section class="split">
  <div class="split-half">
    <div class="ph" role="img" aria-label="Instructor talking to riders at the track" style="background:linear-gradient(90deg,rgba(0,0,0,.75) 0%,rgba(0,0,0,.35) 100%),linear-gradient(160deg,#8a7a66,#3e3428)"></div>
    <h3>Stay Updated</h3>
    <p>Subscribe to our newsletter for race news and events.</p>
    <div class="subscribe"><span>Your email address</span><a class="btn" href="#">Subscribe</a></div>
  </div>
  <div class="split-half">
    <div class="ph" role="img" aria-label="Motocross rider in a red jersey on the track" style="background:linear-gradient(90deg,rgba(80,0,0,.8) 0%,rgba(0,0,0,.35) 100%),linear-gradient(160deg,#9a6a5a,#2a2a2a)"></div>
    <h3>Get In Touch</h3>
    <p>For safety reasons you must have a motocross racing license for fast motocross riding or at least one MX academy course.</p>
    <a class="btn" href="#">Contact Us</a>
  </div>
</section>

<footer class="footer">
  <div class="footer-cols">
    <div class="footer-brand">
      <div class="wordmark"><span class="dot"></span>Saltmarsh</div>
      <p>Are you looking for an extraordinary motocross event? You want to feel the desert sand under the wheels and the thrill of your ride? Be part of our next event!</p>
      <div class="socials"><span></span><span></span><span></span></div>
    </div>
    <div class="footer-col"><h4>Support</h4><ul><li>Home</li><li>School</li><li>Motocross Club</li><li>Safety Course</li><li>Motocross Dubai</li><li>Contact</li></ul></div>
    <div class="footer-col"><h4>Features</h4><ul><li>News</li><li>Events</li><li>Testimonials</li><li>Terms &amp; News</li><li>Wallpapers</li><li>Find a Retailer</li></ul></div>
    <div class="footer-col"><h4>Company</h4><ul><li>About Us</li><li>Members Area</li><li>Sponsorship</li><li>Privacy</li><li>Recall Information</li><li>Global Website</li></ul></div>
  </div>
  <div class="copyright">© 2024 Saltmarsh Motocross Club. All rights reserved.</div>
  <a class="to-top" href="#" aria-label="Back to top"><svg width="14" height="14" viewBox="0 0 24 24"><path fill="none" stroke="#fff" stroke-width="3" d="M5 15l7-7 7 7"/></svg></a>
</footer>

</body>
</html>
```